Postcard For neighbors near worksite

We are a residential interior and exterior painting company. I will be sending post cards out in neighborhoods that we will be currently working in. Basically giving the neighbors a "Neighborhood Notice" that we are in the area and would like to give a Free Estimate to anyone in that neighborhood. I will attach a file of another companies idea that I like. Also, I attached my Logo. Brightfold Painting & More

Target Market(s)

Neighbors near where we are working

Industry/Entity Type

It Company

Requirements
Must have
• Website: Brightfoldpaint.example
• Number: 555.204.6190

```html
<!DOCTYPE html>
<html lang="en">
<head>
<meta charset="utf-8">
<title>Neighborhood Notice Postcard – Brightfold Painting &amp; More</title>
<link rel="stylesheet" href="https://fonts.googleapis.com/css2?family=Oswald:wght@400;700&family=Roboto:wght@700;900&display=swap">
<style>
  :root {
    --red: #e41b1b;
    --red-deep: #b80d0d;
    --red-light: #ff3a32;
    --ink: #111111;
    --white: #ffffff;
    --photo-top: #8c8a72;
    --photo-bottom: #c9a08a;
  }
  * { box-sizing: border-box; margin: 0; padding: 0; }
  html, body { width: 667px; height: 1200px; overflow: hidden; background: var(--white); }
  .postcard {
    position: relative;
    width: 667px;
    height: 1200px;
    overflow: hidden;
    font-family: "Roboto", Arial, sans-serif;
    background: var(--white);
  }
  .hero {
    position: absolute; left: 0; top: 0; width: 667px; height: 368px;
    background: radial-gradient(ellipse at 50% 55%, var(--red-light) 0%, var(--red) 45%, var(--red-deep) 100%);
    border-bottom: 6px solid var(--ink);
    text-align: center;
    color: var(--white);
  }
  .hero-kicker {
    position: absolute; left: 0; right: 0; top: 88px;
    font-family: "Oswald", "Arial Narrow", sans-serif;
    font-weight: 400;
    font-size: 86px;
    line-height: 1;
    letter-spacing: 0;
  }
  .hero-title {
    position: absolute; left: 0; right: 0; top: 168px;
    font-family: "Oswald", "Arial Narrow", sans-serif;
    font-weight: 700;
    font-size: 168px;
    line-height: 1;
    letter-spacing: 2px;
    transform: scaleY(1.12);
    transform-origin: top center;
  }
  .intro {
    position: absolute; left: 0; top: 374px; width: 667px; height: 478px;
    background: var(--white);
  }
  .crew-photo {
    position: absolute; left: 38px; top: 23px; width: 318px; height: 436px;
    background: linear-gradient(180deg, var(--photo-top) 0%, #a78e7b 55%, var(--photo-bottom) 100%);
  }
  .intro-message {
    position: absolute; left: 378px; top: 28px; width: 270px;
    font-weight: 900;
    font-size: 32px;
    line-height: 46px;
    color: var(--ink);
  }
  .services {
    position: absolute; left: 376px; top: 324px;
    list-style: none;
  }
  .services li {
    display: flex; align-items: center;
    height: 46px;
    font-weight: 700; font-size: 20px; color: var(--ink);
  }
  .services svg { width: 22px; height: 22px; margin-right: 9px; flex: none; }
  .offer {
    position: absolute; left: 0; top: 852px; width: 667px; height: 163px;
    background: radial-gradient(ellipse at 50% 40%, var(--red-light) 0%, var(--red) 50%, var(--red-deep) 100%);
    border-top: 5px solid var(--ink);
    text-align: center; color: var(--white);
  }
  .offer-headline {
    margin-top: 24px;
    font-weight: 900; font-size: 32px; line-height: 40px;
  }
  .offer-web {
    margin-top: 8px;
    font-weight: 700; font-size: 23px;
  }
  .contact {
    position: absolute; left: 0; top: 1015px; width: 667px; height: 126px;
    background: var(--white);
  }
  .brand {
    position: absolute; left: 44px; top: 28px; width: 250px;
    display: flex; align-items: center;
  }
  .brand-mark { width: 22px; height: 22px; background: var(--red); flex: none; margin-right: 12px; }
  .brand-name {
    font-weight: 900; font-size: 26px; line-height: 32px; color: var(--red);
  }
  .call {
    position: absolute; left: 300px; top: 18px; width: 367px;
    text-align: center; color: var(--red); font-weight: 900;
  }
  .call-label { font-size: 38px; line-height: 46px; }
  .call-number { font-size: 44px; line-height: 54px; }
  .footer-band {
    position: absolute; left: 0; top: 1141px; width: 667px; height: 59px;
    background: radial-gradient(ellipse at 50% 0%, var(--red-light) 0%, var(--red) 50%, var(--red-deep) 100%);
  }
</style>
</head>
<body>
<main class="postcard">
  <header class="hero">
    <div class="hero-kicker">NEIGHBORHOOD</div>
    <div class="hero-title">NOTICE!</div>
  </header>

  <section class="intro">
    <div class="crew-photo" role="img" aria-label="Photo of the smiling painting crew in white company shirts in front of a freshly painted wall"></div>
    <p class="intro-message">We are currently painting a house in your neighborhood!</p>
    <ul class="services">
      <li><svg viewBox="0 0 22 22" aria-hidden="true"><circle cx="11" cy="11" r="9" fill="none" stroke="#e41b1b" stroke-width="2.5"/><path d="M6.5 11.2l3 3 6-6.2" fill="none" stroke="#111" stroke-width="2.6" stroke-linecap="round" stroke-linejoin="round"/></svg>Interior Painting</li>
      <li><svg viewBox="0 0 22 22" aria-hidden="true"><circle cx="11" cy="11" r="9" fill="none" stroke="#e41b1b" stroke-width="2.5"/><path d="M6.5 11.2l3 3 6-6.2" fill="none" stroke="#111" stroke-width="2.6" stroke-linecap="round" stroke-linejoin="round"/></svg>Exterior Painting</li>
      <li><svg viewBox="0 0 22 22" aria-hidden="true"><circle cx="11" cy="11" r="9" fill="none" stroke="#e41b1b" stroke-width="2.5"/><path d="M6.5 11.2l3 3 6-6.2" fill="none" stroke="#111" stroke-width="2.6" stroke-linecap="round" stroke-linejoin="round"/></svg>General Repairs</li>
    </ul>
  </section>

  <section class="offer">
    <p class="offer-headline">Call for a Free Estimate<br>while we are in the area</p>
    <p class="offer-web">www.brightfoldpaint.example</p>
  </section>

  <section class="contact">
    <div class="brand">
      <span class="brand-mark"></span>
      <span class="brand-name">Brightfold Painting &amp; More</span>
    </div>
    <div class="call">
      <div class="call-label">CALL NOW:</div>
      <div class="call-number">555.204.6190</div>
    </div>
  </section>

  <div class="footer-band"></div>
</main>
</body>
</html>
```